Wine producer needing new wine lables

HI
i require a new wine lable design
must be front and back lable

looking to use only colors of black and gold (shiny gold)

Please look at the image i have uploaded for your reference.

i want the basic concept like that image i have supplied
for the front label please use this information

the bottling location is - South Austtralia
Wine name - Velmont Ridge
Milesime - 2016
under millesime - Cabernet Sauvignon
appellation - Wine of Australia

Sorry I forgot to mention the label is to be 13.5cm high by10.5 cm wide

Target Market(s)

Chinese wine buyers

Logo Text

Corvalle Estate Wines, 2016 cabernet sauvignon, Wine of australia

Logo styles of interest
Emblem Logo
Font styles to use
Decorative

Requirements
Must have
• Must have informtion i have supplied,
• must be black and gold,
• maybe black lable with all imagery and information in gold
• must have a palace/royal building in centre
• Lable must be put on a wine bottle
• Sorry I forgot to mention the label is to be 13.5cm high by10.5 cm wide
Nice to have
• the "palace in the middle" must be original design
• i want the "Palace/building' to look like a royal family lives their
Should not have
• bright colors
• animlas
• please put the label on a wine bottle so we can see properly, will not ecept images that resemble business cards.

```html
<!DOCTYPE html>
<html lang="en">
<head>
<meta charset="utf-8">
<title>Velmont Ridge – Wine Labels</title>
<link rel="stylesheet" href="https://fonts.googleapis.com/css2?family=Cinzel:wght@500;600&family=Cormorant+Garamond:wght@500;600&family=EB+Garamond:wght@400;600&display=swap">
<style>
  :root {
    --page: #ffffff;
    --ink: #000000;
    --gold: #c9a24a;
    --gold-light: #f3dc92;
    --gold-deep: #8c6622;
    --copy: #e9e4d8;
  }
  * { margin: 0; padding: 0; box-sizing: border-box; }
  html, body { width: 1200px; height: 721px; overflow: hidden; background: var(--page); }
  .sheet { position: relative; width: 1200px; height: 721px; }
  .label-block { position: absolute; top: 140px; width: 430px; }
  .label-block--front { left: 49px; }
  .label-block--back { left: 504px; }
  .view-tag {
    font-family: "Cinzel", serif; font-weight: 500; font-size: 11px;
    color: var(--gold); letter-spacing: 0.5px; height: 19px; padding-left: 2px;
  }
  .label { position: relative; width: 430px; height: 482px; }
  .label svg { position: absolute; inset: 0; display: block; }
  .caps { font-family: "Cinzel", serif; font-weight: 600; fill: var(--gold); }
  .wordmark { font-family: "Cormorant Garamond", serif; font-weight: 500; fill: var(--gold); }
  .serif { font-family: "EB Garamond", serif; fill: var(--gold); }
  .serif-light { font-family: "EB Garamond", serif; fill: #f1ece0; }
  .back-copy {
    position: absolute; left: 82px; top: 131px; width: 266px;
    font-family: "EB Garamond", serif; font-size: 7.2px; line-height: 9.4px;
    color: var(--copy); text-align: center;
  }
  .back-copy h3 { font-size: 7.6px; font-weight: 600; margin-bottom: 8px; }
  .back-copy p { margin-bottom: 7px; }
  .back-copy .translation-head { margin-bottom: 0; }
</style>
</head>
<body>
<svg width="0" height="0" style="position:absolute" aria-hidden="true">
  <defs>
    <linearGradient id="goldFoil" x1="0" y1="0" x2="1" y2="1">
      <stop offset="0" stop-color="#8c6622"/>
      <stop offset="0.25" stop-color="#f3dc92"/>
      <stop offset="0.5" stop-color="#b8892f"/>
      <stop offset="0.75" stop-color="#f0d588"/>
      <stop offset="1" stop-color="#8c6622"/>
    </linearGradient>
    <linearGradient id="ornamentTone" x1="0" y1="0" x2="0" y2="1">
      <stop offset="0" stop-color="#e8c977"/>
      <stop offset="1" stop-color="#a57b2c"/>
    </linearGradient>
  </defs>
</svg>

<main class="sheet">
  <section class="label-block label-block--front">
    <div class="view-tag">Front</div>
    <div class="label">
      <svg viewBox="0 0 430 482" width="430" height="482">
        <path class="label-shape" fill="var(--ink)" d="M6,0 H424 Q430,0 430,6 V230 C430,392 330,482 215,482 C100,482 0,392 0,230 V6 Q0,0 6,0 Z"/>
        <path class="frame-band" fill="none" stroke="url(#goldFoil)" stroke-width="7" d="M15,15 H415 V230 C415,380 322,467 215,467 C108,467 15,380 15,230 Z"/>
        <path class="frame-line" fill="none" stroke="url(#goldFoil)" stroke-width="1.6" d="M25,25 H405 V230 C405,370 318,455 215,455 C112,455 25,370 25,230 Z"/>
        <text class="caps" x="215" y="63" text-anchor="middle" font-size="16" letter-spacing="2">South Austtralia</text>
        <rect x="140" y="118" width="155" height="76" rx="4" fill="url(#ornamentTone)" role="img" aria-label="Gold crown crest with scroll flourish"/>
        <text class="wordmark" x="215" y="236" text-anchor="middle" font-size="38" letter-spacing="0.5">VELMONT RIDGE</text>
        <text class="serif" x="215" y="345" text-anchor="middle" font-size="25">2016</text>
        <path id="frontArc" fill="none" d="M100,300 A122.7 122.7 0 0 0 330,300"/>
        <text class="caps" font-size="21"><textPath href="#frontArc" startOffset="50%" text-anchor="middle" textLength="276" lengthAdjust="spacing">Cabernet Sauvignon</textPath></text>
        <text class="serif-light" x="83" y="393" font-size="14">17.5ml</text>
        <text class="serif-light" x="346" y="393" font-size="14" text-anchor="end">75cl</text>
        <text class="serif-light" x="215" y="422" text-anchor="middle" font-size="17">Wine of Australia</text>
      </svg>
    </div>
  </section>

  <section class="label-block label-block--back">
    <div class="view-tag">Front</div>
    <div class="label">
      <svg viewBox="0 0 430 482" width="430" height="482">
        <path class="label-shape" fill="var(--ink)" d="M6,0 H424 Q430,0 430,6 V230 C430,392 330,482 215,482 C100,482 0,392 0,230 V6 Q0,0 6,0 Z"/>
        <path class="frame-band" fill="none" stroke="url(#goldFoil)" stroke-width="7" d="M15,15 H415 V230 C415,380 322,467 215,467 C108,467 15,380 15,230 Z"/>
        <path class="frame-line" fill="none" stroke="url(#goldFoil)" stroke-width="1.6" d="M25,25 H405 V230 C405,370 318,455 215,455 C112,455 25,370 25,230 Z"/>
        <rect x="188" y="38" width="54" height="36" rx="3" fill="url(#ornamentTone)" role="img" aria-label="Small gold crown crest with flourish"/>
        <text class="wordmark" x="215" y="97" text-anchor="middle" font-size="24">VELMONT RIDGE</text>
        <text class="caps" x="215" y="110" text-anchor="middle" font-size="8.5" letter-spacing="1">South Austtralia</text>
        <text class="serif" x="215" y="395" text-anchor="middle" font-size="16">2016</text>
        <path id="backArc" fill="none" d="M148,370 A72 72 0 0 0 284,370"/>
        <text class="caps" font-size="13"><textPath href="#backArc" startOffset="50%" text-anchor="middle" textLength="170" lengthAdjust="spacing">Cabernet Sauvignon</textPath></text>
        <text class="serif-light" x="215" y="437" text-anchor="middle" font-size="11">Wine of Australia</text>
      </svg>
      <div class="back-copy">
        <h3>The standard Lorem Ipsum passage, used since the 1500s</h3>
        <p>"Lorem ipsum dolor sit amet, consectetur adipiscing elit, sed do eiusmod tempor incididunt ut labore et dolore magna aliqua.</p>
        <p>Section 1.10.32 of "de Finibus Bonorum et Malorum", written by Varennus in 45 BC</p>
        <p>"Sed ut perspiciatis unde omnis iste natus error sit voluptatem accusantium doloremque laudantium, totam rem aperiam, eaque ipsa quae ab illo inventore veritatis et quasi architecto beatae vitae dicta sunt explicabo. qui ratione voluptatem sequi nesciunt.</p>
        <h3 class="translation-head">1914 translation by H. Dorvel</h3>
        <p>"But I must explain to you how all this mistaken idea of denouncing pleasure and praising pain was born and I will give you a complete account of the system.</p>
        <p>Section 1.10.33 of "de Finibus Bonorum et Malorum", written by Varennus in 45 BC</p>
        <p>"At vero eos et accusamus et iusto odio dignissimos ducimus qui blanditiis praesentium voluptatum deleniti atque corrupti quos dolores et quas molestias excepturi sint occaecati cupiditate non provident, similique sunt in culpa qui officia deserunt mollitia animi, id est laborum et dolorum fuga.</p>
      </div>
    </div>
  </section>
</main>
</body>
</html>
```